Simple but impressive brochure for Consulting Company

We need a single page (back and front) brochure to introduce our company to prospective clients. We are open to different formats, but think that a trifold or double fold may work best. (fold up style brochure or a flyer with front & back).

It should be easy to print as we will need to print it as soon as possible. 8 1/2 x 11 based format is probably best, but again, we are open to suggestions.

About the Company:

We are a consulting company comprised of US Navy fighter pilots (SKYLANCE), US Navy SEALS, and business executives, that use our knowledge and experience in high risk / high performance environments to benefit our business clients. Most of our clients are in the oil and mining sector.

We deal with drilling companies and their crews and management. We do lectures and provide on-site training and coaching.

Enclosed in the "file" section are various one page handouts with information that describes what we do and how we currently project our image to our clients.

Our website is http://www.veltmorix.example

We have photographs of worksites, fighter jets, etc. available for creative use, if the quality is deemed acceptable by you, the designer, to use. We are not opposed to stock photos if those would be preferable.

We are working on a fairly tight schedule as we have an event on 4 February 2013. So we need the design done and enough time to have the final version printed. We set this project at 5 days, but can extend it a bit as needed.

We are looking for a design that is solid, professional and gives an indication of our background in high risk environments, but does not over emphasis our military experience.

Oil field related imagery would be a nice addition. In our business, we emphasis and sell the concept of SAFE and RELIABLE operations, done by people with vast experience in the field.

We take our experience in the field and aircraft carrier operations and pass those lessons to the oil field and mining operations. (primarily oil field)

In case you need to know: we have a few different versions of our LOGO in the attached files. It consists of an orb and the word KESTRAN in "Good Times" font, slightly flattened and stretched. (you can see the logo files). We also use a Kestran AXIS(tm) logo for a specific set of programs we offer.

Note: We have more files to upload, but currently it is maxed at 5 files. They will be uploaded if more are allowed or put in a Filevat.

Thank you all for your participation.  I'm sorry I could only pick one design, as so many of you are very talented and made the choice difficult.

Target Market(s)

Our buyers are managers and executives of Meridel 400 companies. Primarily male, educated, many with engineering backgrounds.

Industry/Entity Type

Training

Requirements
Must have
• Our primary desire is to convey a sense of action and professionalism to our prospective clients. I'm not sure if we have anything compulsory required with the exception of our logo.

If there is room and it makes sense, we can include the "Service Disabled Veteran" logo. (in file section)

Nice to have
• We would like an ongoing relationship with our selected designer. We will have updated brochures and web graphics in the near future.

```html
<!DOCTYPE html>
<html lang="en">
<head>
<meta charset="utf-8">
<title>Kestran Brochure Spread</title>
<link href="https://fonts.googleapis.com/css2?family=Questrial&display=swap" rel="stylesheet">
<style>
  :root {
    --cyan: #19b4ea;
    --teal: #10a6bd;
    --red: #e41f2d;
    --ink: #6b6b6b;
    --paper: #ffffff;
    --divider: #222222;
  }
  * { margin: 0; padding: 0; box-sizing: border-box; }
  html, body { width: 1200px; height: 929px; overflow: hidden; background: var(--paper); }
  body { position: relative; font-family: "Questrial", "Helvetica Neue", Arial, sans-serif; color: var(--ink); }
  .spread { position: absolute; inset: 0; width: 1200px; height: 929px; }
  .page-divider { position: absolute; left: 595px; top: 0; width: 2px; height: 929px; background: var(--divider); }
  .shapes { position: absolute; inset: 0; }
  .copy { position: absolute; }
  .copy h2 {
    font-weight: 400; color: var(--cyan); font-size: 26.5px; line-height: 30px; margin-bottom: 2px;
  }
  .copy p {
    font-size: 14.8px; line-height: 18px; text-align: justify; letter-spacing: 0.35px;
  }
  .copy-left { left: 57px; top: 473px; width: 478px; }
  .copy-left p { margin-bottom: 8px; }
  .copy-left p.lead { margin-bottom: 5px; }
  .copy-right { left: 655px; top: 80px; width: 470px; }
  .copy-right p { margin-bottom: 6px; }
  .copy-right .gap { margin-bottom: 12px; }
</style>
</head>
<body>
<main class="spread">
  <svg class="shapes" width="1200" height="929" viewBox="0 0 1200 929">
    <defs>
      <linearGradient id="teamTone" x1="0" y1="0" x2="1" y2="1">
        <stop offset="0" stop-color="#3aa7b8"/>
        <stop offset="0.45" stop-color="#c9cdd2"/>
        <stop offset="1" stop-color="#2b3440"/>
      </linearGradient>
      <linearGradient id="seaTone" x1="0" y1="0" x2="0" y2="1">
        <stop offset="0" stop-color="#4c9ad8"/>
        <stop offset="1" stop-color="#0f5fb4"/>
      </linearGradient>
    </defs>

    <polygon class="band-top" points="0,0 298,0 338,86 0,86" fill="var(--cyan)"/>
    <polygon class="band-teal-edge" points="0,62 30,62 30,400 0,400" fill="var(--teal)"/>
    <polygon class="band-under" points="125,398 500,398 530,438 148,438" fill="var(--cyan)"/>
    <polygon class="band-under-teal" points="0,398 190,398 210,420 0,420" fill="var(--teal)"/>
    <polygon role="img" aria-label="Photo of three smiling business professionals in suits"
      points="32,86 437,86 590,398 0,398 0,128" fill="url(#teamTone)"/>
    <polygon class="accent-red" points="114,338 134,338 198,445 172,445" fill="var(--red)"/>

    <polygon role="img" aria-label="Photo of a fighter jet flying over an offshore oil rig and support vessels at sea"
      points="662,547 1090,547 1189,853 828,853" fill="url(#seaTone)"/>
    <polygon class="accent-cyan" points="688,648 740,648 820,820 790,820" fill="var(--cyan)"/>
    <polygon class="accent-red" points="805,790 830,790 876,880 850,880" fill="var(--red)"/>
  </svg>

  <div class="page-divider"></div>

  <section class="copy copy-left">
    <div class="block-about">
      <h2>ABOUT KESTRAN</h2>
      <p class="lead">Kestran is a high performance training and consulting company with high performance people. Kestran's team consists of Fighter Pilots, Navy SEALS, Special Forces, Astronauts, and veteran industry &amp; corporate leaders. We leverage the credibility, experience, expertise, and ingenuity of our team to develop solutions for our clients.</p>
    </div>
    <div class="block-mission">
      <h2>Kestran's Mission</h2>
      <p class="lead">Optimize Safety And Operational Excellence In Complex High-Risk Arenas.</p>
    </div>
    <div class="block-foundation">
      <h2>Foundation of Excellence</h2>
      <p>The Foundation of Excellence is built on vision, leadership, communication, and teamwork. Using Kestran practices, high performance companies execute toward a crystal clear strategic vision that leadership clearly communicates to frontline teams and individuals.</p>
      <p>Kestran's solutions accelerate the realization of an organization's vision.</p>
    </div>
  </section>

  <section class="copy copy-right">
    <div class="block-engine">
      <h2>Engine of Excellence</h2>
      <p>Kestran instills the disciplines of Planning, Briefing, Execution, and the After Action Review (AAR) that raise levels of excellence and drive continuous improvement within an organization.</p>
      <p class="gap">The Engine of Excellence yields consistent and predictable results. Our proprietary programs provide disciplined methodologies that create deliberate actions for advancing your organization's vision.</p>
    </div>
    <div class="block-human">
      <h2>Human Performance</h2>
      <p class="gap">The human element is the most important factor for success in complex high-risk organizations. Kestran laser- focuses on the strengths and weaknesses of the human component. Our solutions are built to optimize leadership, decision-making, situational awareness, communications, teamwork, and more.</p>
    </div>
    <div class="block-axis">
      <h2>Kestran AXIS&trade;</h2>
      <p>The drive toward zero incidents is the hallmark of high-performing complex high-risk organizations. Our Kestran AXIS&trade; family of programs builds the skill sets required for organizations and individuals to embark on a true Path of Excellence.</p>
    </div>
  </section>
</main>
</body>
</html>
```